New more attractive design for an old tired look that is high tech but inviting

Need a more modern eye catching design. We are and I/T and MSP and we need a new look. Need a call to action on each page. Needs to be in WordPress. Existing site is brivanoqe.com. Needs to work on phones and tablets. The default home page should present us as an MSP/MSSP and direct the viewer to our services we offer.
Updates

Current deadline assigned at project inception has passed before project started

Need extra days to review

Target Market(s)

Our target market is other businesses. We do not target residential customers.

Industry/Entity Type

Business to Business oriented

Coding

Coded - Design and coding required

Number of Pages Required

5+ page

Font styles to use
Sans Serif

Requirements
Must have
• Must have a current relevant design with a call to action on each page.
Nice to have
• Dark background high tech look with people to make it attractive

```html
<!DOCTYPE html>
<html lang="en">
<head>
<meta charset="utf-8">
<title>Corvane Solutions – Data Center Services</title>
<link href="https://fonts.googleapis.com/css2?family=Cabin:wght@500;600&family=Lato:wght@400;700&family=Poppins:wght@400;500&family=Crimson+Text:wght@400&display=swap" rel="stylesheet">
<style>
:root{
  --red:#e0202a;
  --red-dark:#b3141c;
  --ink:#1d1d1f;
  --text:#4a4a4a;
  --pink:#fdd9dc;
  --white:#ffffff;
  --navy:#0b1a2c;
  --blue:#1f5d95;
}
*{box-sizing:border-box;margin:0;padding:0}
html,body{width:1200px;height:3542px;overflow:hidden;background:var(--white)}
body{position:relative;font-family:"Lato",sans-serif;color:var(--text)}
.abs{position:absolute}
.btn{position:absolute;display:flex;align-items:center;justify-content:center;background:var(--red);color:var(--white);font-family:"Lato",sans-serif;font-weight:700;font-size:17px;border-radius:24px;text-decoration:none}
h1,h2,h3{font-family:"Cabin",sans-serif;font-weight:500;color:var(--ink)}
.accent{color:var(--red);font-weight:600}

/* header */
.brand{position:absolute;left:108px;top:22px;color:var(--white);font-family:"Cabin",sans-serif;font-weight:600;font-size:40px;line-height:44px}
.brand span{display:block;padding-left:74px;font-weight:500}
.nav{position:absolute;top:35px;font-family:"Poppins",sans-serif;font-size:15px;color:var(--ink)}
.nav.active{color:var(--red)}
.nav.active::after{content:"";position:absolute;left:0;right:0;top:27px;height:2px;background:var(--red)}

/* hero */
.hero-title{position:absolute;left:110px;top:224px;font-size:52px;color:var(--white);font-weight:600;text-shadow:0 2px 6px rgba(0,0,0,.4)}
.hero-text{position:absolute;left:112px;top:308px;width:430px;color:var(--white);font-size:15px;line-height:27px}

/* about */
.media{position:absolute;border-radius:8px;overflow:hidden}
.about-photo{left:111px;top:764px;width:444px;height:382px;
  background:
    radial-gradient(ellipse 90px 160px at 78% 48%,rgba(20,30,45,.85),transparent 70%),
    radial-gradient(ellipse 120px 90px at 62% 58%,rgba(90,180,255,.55),transparent 70%),
    radial-gradient(ellipse 70px 260px at 18% 55%,rgba(60,140,230,.55),transparent 70%),
    repeating-linear-gradient(90deg,rgba(255,255,255,.04) 0 3px,transparent 3px 22px),
    linear-gradient(120deg,#0d2440 0%,#1d5c94 45%,#0a1a30 100%)}
.play{position:absolute;left:175px;top:166px;width:84px;height:84px;border-radius:50%;background:rgba(255,255,255,.35);border:2px solid rgba(255,255,255,.6)}
.badge{position:absolute;left:470px;top:1034px;width:129px;height:129px;background:linear-gradient(#fff 55%,#fde3e5);border-radius:8px;box-shadow:0 6px 12px rgba(0,0,0,.2);text-align:center;color:var(--red);font-family:"Cabin",sans-serif}
.badge b{display:block;font-size:40px;font-weight:500;margin-top:18px;line-height:40px}
.badge span{font-size:21px;line-height:26px}
.about-title{position:absolute;left:640px;top:752px;font-size:41px;line-height:52px}
.about-text{position:absolute;left:639px;top:874px;width:430px;font-size:14.5px;line-height:28px}

/* services */
.section-title{position:absolute;left:0;width:1200px;text-align:center;font-size:42px}
.svc-img{top:1408px;height:284px;border-radius:10px}
.svc-label{position:absolute;top:1714px;width:310px;text-align:center;font-family:"Cabin",sans-serif;font-size:26px;color:var(--ink)}
.svc-overlay{position:absolute;left:27px;top:82px;width:260px;color:var(--white);font-size:15px;line-height:27.5px}
.svc-dot{position:absolute;left:225px;top:237px;width:70px;height:70px;border-radius:50%;background:var(--white);box-shadow:0 2px 6px rgba(0,0,0,.2);display:flex;align-items:center;justify-content:center}

/* feature cards */
.card{position:absolute;top:2080px;height:355px;background:var(--white);border-radius:10px;box-shadow:0 2px 10px rgba(0,0,0,.18);overflow:hidden}
.card .img{height:157px}
.card h3{font-size:23px;margin:14px 0 0 17px}
.card p{margin:4px 14px 0 17px;font-size:14.5px;line-height:27.5px}
.card .btn{left:11px;bottom:14px;width:148px;height:46px}

/* contact */
.contact-title{position:absolute;left:108px;top:2676px;font-size:41px;color:var(--white);font-weight:600}
.contact-line{position:absolute;left:155px;color:var(--white);font-size:15px;line-height:28px}
.c-icon{position:absolute;left:110px;width:28px;height:28px;border-radius:50%;background:var(--white)}
.form{position:absolute;left:599px;top:2676px;width:525px;height:427px;background:var(--white)}
.field{position:absolute;left:43px;width:444px;border:1px solid #9a9a9a;font-size:15px;color:#555;padding-left:48px;display:flex;align-items:center}
.field svg{position:absolute;left:14px}
.send{position:absolute;left:43px;top:344px;width:444px;height:47px;background:var(--red);color:var(--white);display:flex;align-items:center;justify-content:center;font-weight:700;font-size:17px}

/* footer */
.foot-head{position:absolute;top:3244px;font-family:"Crimson Text",serif;font-size:22px;color:var(--red)}
.quick{position:absolute;left:152px;top:3282px;list-style:none;font-family:"Poppins",sans-serif;font-size:15px;color:var(--ink);line-height:29px}
.quick li::before{content:"";display:inline-block;width:7px;height:7px;background:var(--red);margin-right:13px;vertical-align:2px}
.foot-brand{position:absolute;left:460px;top:3256px;width:320px;font-family:"Cabin",sans-serif;font-weight:600;font-size:52px;line-height:52px;color:var(--ink)}
.foot-brand span{display:block;padding-left:96px;font-weight:500}
.social{position:absolute;top:3380px;width:28px;height:28px;border-radius:50%}
.fc-line{position:absolute;left:905px;font-size:15px;color:var(--ink);line-height:28px}
.fc-icon{position:absolute;left:866px;width:22px;height:22px}
.rule{position:absolute;left:108px;top:3478px;width:976px;height:1px;background:#bbb}
.copy{position:absolute;left:0;width:1200px;top:3494px;text-align:center;font-size:15px;color:var(--ink)}
</style>
</head>
<body>

<!-- Hero -->
<svg class="abs" style="left:0;top:0" width="1200" height="690" role="img" aria-label="Photo of two engineers reviewing a laptop between server racks in a data center">
  <defs>
    <linearGradient id="heroFill" x1="0" y1="0" x2="1" y2="0.3">
      <stop offset="0" stop-color="#05080e"/>
      <stop offset="0.3" stop-color="#141c27"/>
      <stop offset="0.55" stop-color="#3b4756"/>
      <stop offset="0.78" stop-color="#1f5f9c"/>
      <stop offset="1" stop-color="#0a2140"/>
    </linearGradient>
    <radialGradient id="heroGlowA" cx="0.88" cy="0.4" r="0.25">
      <stop offset="0" stop-color="#5fb2ff" stop-opacity=".55"/>
      <stop offset="1" stop-color="#5fb2ff" stop-opacity="0"/>
    </radialGradient>
    <radialGradient id="heroGlowB" cx="0.55" cy="0.35" r="0.22">
      <stop offset="0" stop-color="#8a96a4" stop-opacity=".55"/>
      <stop offset="1" stop-color="#8a96a4" stop-opacity="0"/>
    </radialGradient>
    <radialGradient id="heroGlowC" cx="0.66" cy="0.5" r="0.18">
      <stop offset="0" stop-color="#2a3340" stop-opacity=".8"/>
      <stop offset="1" stop-color="#2a3340" stop-opacity="0"/>
    </radialGradient>
    <clipPath id="heroClip">
      <path d="M14,26 Q14,11 29,11 L372,11 L410,92 L1168,92 Q1185,92 1185,109 L1185,662 Q1185,679 1168,679 L398,679 L352,601 L30,601 Q14,601 14,585 Z"/>
    </clipPath>
  </defs>
  <g clip-path="url(#heroClip)">
    <rect width="1200" height="690" fill="url(#heroFill)"/>
    <rect width="1200" height="690" fill="url(#heroGlowA)"/>
    <rect width="1200" height="690" fill="url(#heroGlowB)"/>
    <rect width="1200" height="690" fill="url(#heroGlowC)"/>
  </g>
</svg>
<div class="brand">Corvane<span>Solutions</span></div>
<a class="nav active" style="left:482px">Home</a>
<a class="nav" style="left:558px">About</a>
<a class="nav" style="left:635px">Services</a>
<a class="nav" style="left:727px">Testimonials</a>
<a class="btn" style="left:938px;top:25px;width:148px;height:46px">Contact Us</a>
<h1 class="hero-title">Data Center Services</h1>
<p class="hero-text">We offer colocation, virtualization, storage as a service and disaster recovery out of our own enterprise-grade data center.</p>
<a class="btn" style="left:112px;top:395px;width:150px;height:46px">Get Started</a>

<!-- About -->
<div class="media about-photo" role="img" aria-label="Video thumbnail of an engineer working on a laptop in a server room">
  <div class="play"><svg width="84" height="84"><path d="M35,28 L58,42 L35,56 Z" fill="#e0202a"/></svg></div>
</div>
<div class="badge"><b>22</b><span>years in<br>business</span></div>
<h2 class="about-title">About <span class="accent">Corvane</span><br>Solutions</h2>
<p class="about-text">Like most great businesses Corvane Solutions began in a garage during the summer of 1995 in Marlow Ridge, SC. It was a part time venture by Daniel Hartwell and his business partner Owen Pryce. They had discovered an opportunity in technology sales and service after a combined 30 years at Northgate Power in information technology. By 2000, the two set out on their own and were working on the venture full-time.</p>
<a class="btn" style="left:641px;top:1099px;width:149px;height:46px">Read More</a>

<!-- Services -->
<svg class="abs" style="left:0;top:1240px" width="1200" height="680">
  <path d="M14,20 Q14,5 29,5 L1170,5 Q1185,5 1185,20 L1185,659 Q1185,674 1170,674 L398,674 L350,592 L29,592 Q14,592 14,577 Z" fill="var(--pink)"/>
</svg>
<h2 class="section-title" style="top:1320px">Our <span class="accent">Services</span></h2>
<div class="media svc-img" style="left:110px;width:307px;background:
    radial-gradient(ellipse 90px 120px at 60% 45%,rgba(150,170,200,.6),transparent 70%),
    radial-gradient(ellipse 110px 70px at 45% 80%,rgba(40,60,80,.9),transparent 70%),
    radial-gradient(ellipse 60px 200px at 12% 50%,rgba(60,170,190,.5),transparent 70%),
    linear-gradient(110deg,#071622,#1c4f66 45%,#0f2433)" role="img" aria-label="Photo of a technician with a laptop beside network cabling"></div>
<div class="media svc-img" style="left:441px;width:310px;border:3px solid var(--red);background:
    radial-gradient(ellipse 60px 140px at 50% 70%,rgba(90,170,255,.45),transparent 70%),
    repeating-linear-gradient(90deg,rgba(120,190,255,.08) 0 4px,transparent 4px 26px),
    linear-gradient(#081530,#1a4f86 60%,#0b1e3a)" role="img" aria-label="Photo of a server aisle in a data center">
  <p class="svc-overlay">Our data center is a Tier III, standalone structure designed to withstand wind speeds up to 206mph. We have fully redundant power, cooling and internet<br>Read More...</p>
  <div class="svc-dot">
    <svg width="40" height="40" viewBox="0 0 40 40" fill="none" stroke="#e0202a" stroke-width="2">
      <rect x="6" y="5" width="28" height="8" rx="1"/>
      <rect x="6" y="16" width="28" height="8" rx="1"/>
      <rect x="6" y="27" width="28" height="8" rx="1"/>
      <circle cx="11" cy="9" r="1.2" fill="#e0202a"/>
      <circle cx="11" cy="20" r="1.2" fill="#e0202a"/>
      <circle cx="11" cy="31" r="1.2" fill="#e0202a"/>
      <path d="M17,9 H29 M17,20 H29 M17,31 H29"/>
    </svg>
  </div>
</div>
<div class="media svc-img" style="left:776px;width:307px;background:
    radial-gradient(ellipse 130px 70px at 55% 85%,rgba(200,170,150,.55),transparent 70%),
    radial-gradient(ellipse 80px 60px at 45% 30%,rgba(255,255,255,.6),transparent 70%),
    radial-gradient(ellipse 200px 100px at 50% 100%,rgba(60,70,85,.55),transparent 70%),
    linear-gradient(120deg,#6f8aa3,#c3cfdb 50%,#e6ebf0)" role="img" aria-label="Photo of hands typing on a laptop with support icons overlaid"></div>
<div class="svc-label" style="left:108px">Cybersecurity</div>
<div class="svc-label" style="left:445px;color:var(--red)">Data Center Services</div>
<div class="svc-label" style="left:775px">Office IT Support</div>
<a class="btn" style="left:522px;top:1781px;width:148px;height:46px">View More</a>

<!-- Features -->
<h2 class="section-title" style="top:1993px;font-size:41px">Your <span class="accent">data center</span>, your way</h2>
<div class="card" style="left:111px;width:304px">
  <div class="img" style="background:
      radial-gradient(ellipse 80px 45px at 50% 38%,rgba(110,200,255,.75),transparent 70%),
      radial-gradient(ellipse 160px 30px at 50% 95%,rgba(40,140,220,.5),transparent 70%),
      linear-gradient(#07101e,#123a5e 65%,#081626)" role="img" aria-label="Illustration of a glowing cloud above a laptop"></div>
  <h3>A True Partner</h3>
  <p>One size data center architecture does not fit all. We take the time to understand your specific requirements.</p>
  <a class="btn">Read More</a>
</div>
<div class="card" style="left:446px;width:305px">
  <div class="img" style="background:
      radial-gradient(ellipse 45px 55px at 50% 45%,rgba(255,60,110,.8),transparent 70%),
      radial-gradient(ellipse 160px 40px at 50% 90%,rgba(255,120,60,.35),transparent 70%),
      linear-gradient(90deg,#10142e,#3a1638 50%,#0d1836)" role="img" aria-label="Illustration of a security shield on a circuit board"></div>
  <h3>High Security</h3>
  <p>Our data center is a Tier III, standalone structure designed to withstand wind speeds up to 206mph. We have fully</p>
  <a class="btn">Read More</a>
</div>
<div class="card" style="left:780px;width:306px">
  <div class="img" style="background:
      radial-gradient(ellipse 40px 90px at 50% 70%,rgba(180,230,255,.7),transparent 70%),
      repeating-linear-gradient(90deg,rgba(150,210,255,.12) 0 3px,transparent 3px 18px),
      linear-gradient(90deg,#0a2550,#2a78bb 50%,#0a2550)" role="img" aria-label="Photo of a long aisle of server racks"></div>
  <h3>Availability</h3>
  <p>The facility is powered by two separate utility feeds and a Halden diesel generator. We utilize multiple in-row</p>
  <a class="btn">Read More</a>
</div>

<!-- Contact -->
<svg class="abs" style="left:0;top:2520px" width="1200" height="650" role="img" aria-label="Red tinted photo of server racks">
  <defs>
    <linearGradient id="contactFill" x1="0" y1="0" x2="1" y2="1">
      <stop offset="0" stop-color="#c81d28"/>
      <stop offset="0.5" stop-color="#a3121c"/>
      <stop offset="1" stop-color="#d22a33"/>
    </linearGradient>
    <radialGradient id="contactGlowA" cx="0.08" cy="0.7" r="0.2">
      <stop offset="0" stop-color="#ff8a8a" stop-opacity=".45"/>
      <stop offset="1" stop-color="#ff8a8a" stop-opacity="0"/>
    </radialGradient>
    <radialGradient id="contactGlowB" cx="0.4" cy="0.45" r="0.25">
      <stop offset="0" stop-color="#6e0910" stop-opacity=".6"/>
      <stop offset="1" stop-color="#6e0910" stop-opacity="0"/>
    </radialGradient>
    <pattern id="rackLines" width="24" height="650" patternUnits="userSpaceOnUse">
      <rect width="2" height="650" fill="#ffffff" opacity=".05"/>
    </pattern>
    <clipPath id="contactClip">
      <path d="M14,22 Q14,7 29,7 L350,7 L408,85 L1170,85 Q1185,85 1185,100 L1185,629 Q1185,644 1170,644 L398,644 L350,572 L29,572 Q14,572 14,557 Z"/>
    </clipPath>
  </defs>
  <g clip-path="url(#contactClip)">
    <rect width="1200" height="650" fill="url(#contactFill)"/>
    <rect width="1200" height="650" fill="url(#rackLines)"/>
    <rect width="1200" height="650" fill="url(#contactGlowA)"/>
    <rect width="1200" height="650" fill="url(#contactGlowB)"/>
  </g>
</svg>
<h2 class="contact-title">Let's get in touch</h2>
<p class="contact-line" style="left:111px;top:2746px">We're open for any suggestion or just to have a chat.</p>
<div class="c-icon" style="top:2798px"><svg width="28" height="28"><path d="M9,8 L12,8 L13,12 L11,13 Q13,17 16,18 L17,16 L21,17 L21,20 Q14,21 8,12 Z" fill="#e0202a"/></svg></div>
<p class="contact-line" style="top:2798px">555-204-7813.</p>
<div class="c-icon" style="top:2843px"><svg width="28" height="28"><rect x="7" y="9" width="14" height="10" fill="#e0202a"/><path d="M7,9 L14,15 L21,9" stroke="#fff" stroke-width="1.5" fill="none"/></svg></div>
<p class="contact-line" style="top:2843px">support@brivanoqe.com</p>
<div class="c-icon" style="top:2887px"><svg width="28" height="28"><path d="M14,6 Q20,6 20,12 Q20,16 14,22 Q8,16 8,12 Q8,6 14,6 Z" fill="#e0202a"/><circle cx="14" cy="12" r="2.5" fill="#fff"/></svg></div>
<p class="contact-line" style="top:2886px">Corvane Solutions<br>48 Quarry Loop<br>Marlow Ridge, SC 29001<br>Open in Maps</p>

<form class="form">
  <div class="field" style="top:45px;height:48px"><svg width="20" height="20"><circle cx="10" cy="6" r="4" fill="#777"/><path d="M2,19 Q10,8 18,19 Z" fill="#777"/></svg>Full Name</div>
  <div class="field" style="top:115px;height:48px"><svg width="22" height="20"><rect x="1" y="4" width="20" height="13" fill="none" stroke="#777" stroke-width="2"/><path d="M1,4 L11,12 L21,4" stroke="#777" stroke-width="2" fill="none"/></svg>Email</div>
  <div class="field" style="top:187px;height:130px;align-items:flex-start;padding-top:15px"><svg width="22" height="20" style="top:14px"><ellipse cx="11" cy="9" rx="9" ry="7" fill="#777"/><path d="M5,14 L3,19 L10,15 Z" fill="#777"/></svg>Message</div>
  <div class="send">Send</div>
</form>

<!-- Footer -->
<h3 class="foot-head" style="left:151px">Quick Links</h3>
<ul class="quick">
  <li>Home</li><li>About</li><li>Services</li><li>Testimonials</li><li>Contact</li>
</ul>
<div class="foot-brand">Corvane<span>Solutions</span></div>
<span class="social" style="left:555px;background:var(--red)"></span>
<span class="social" style="left:595px;background:#b9b9b9"></span>
<span class="social" style="left:635px;background:#b9b9b9"></span>
<h3 class="foot-head" style="left:866px">Contact Us</h3>
<svg class="fc-icon" style="top:3290px" width="22" height="22"><circle cx="11" cy="11" r="11" fill="#e0202a"/><path d="M7,6 L9,6 L10,9 L8.5,10 Q10,13 12,14 L13,12.5 L16,13.5 L16,16 Q10,16.5 6,9 Z" fill="#fff"/></svg>
<p class="fc-line" style="top:3286px">888 888 888</p>
<svg class="fc-icon" style="top:3330px" width="22" height="22"><circle cx="11" cy="11" r="11" fill="#e0202a"/><rect x="6" y="7.5" width="10" height="7" fill="#fff"/><path d="M6,7.5 L11,11.5 L16,7.5" stroke="#e0202a" fill="none"/></svg>
<p class="fc-line" style="top:3326px">info@elmcourtdental.com</p>
<svg class="fc-icon" style="top:3370px" width="22" height="22"><path d="M11,1 Q19,1 19,9 Q19,14 11,21 Q3,14 3,9 Q3,1 11,1 Z" fill="#e0202a"/><circle cx="11" cy="9" r="3" fill="#fff"/></svg>
<p class="fc-line" style="top:3366px">Elmcourt Dental<br>77 Harbor Lane<br>Elmcourt, CA 90001</p>
<div class="rule"></div>
<p class="copy">Copyright 2025 © Corvane Solutions of SC, Inc.</p>

</body>
</html>
```